DL Flyer and magnet design

I am in need of a new flyer design to show some offers on each side. First side Water filtration. Second side Heat pump hot water. I will attach an existing design from a previous flyer/magnet. I have also got some information to go on the flyer and images/logo.

Side 1: Water Filtration Solutions
Coral Ridge Pipeworks and Heating
Fresh, Clean Water for Every Tap

Water Filtration Solutions
1️⃣ High Flow Water Filtration
Starting from just $550!

2️⃣ Whole House Water Filtration
Enjoy pure water throughout your home – starting from $1800!

3️⃣ Whole House Water Filtration with UV Lamp (Perfect for rainwater systems)
Get the ultimate filtration – starting from $3000!

🎁 FREE BRAVO COOLER
With every water filtration system or referral!

📞 Call us today: 0491 837 254
🌐 Visit our website: www.coralridgeph.example.au

💧 Better water, better life. Call now for a free quote!

Side 2: Heat Pump Hot Water Systems
Energy-Efficient Hot Water Solutions

Heat Pump Hot Water Systems
🌟 Rebates Available!
Save big with government incentives on energy-efficient hot water systems.

💼 All Major Makes, Models, and Sizes
We supply and install trusted brands to suit your household’s needs.

💳 Interest-Free Finance Options
Upgrade now and pay later with flexible payment plans.

🎁 FREE BRAVO COOLER
With every heat pump system or referral!

💧 Upgrade to energy-efficient hot water and save!

Please include on the flyer. Valid until 30/6/2-25 Images are for illustrative purposes only and may not represent the exact product or service provided

```html
<!DOCTYPE html>
<html lang="en">
<head>
<meta charset="utf-8">
<title>Coral Ridge Pipeworks and Heating – DL Flyer</title>
<link href="https://fonts.googleapis.com/css2?family=Poppins:wght@300;400;600;700;800&display=swap" rel="stylesheet">
<style>
  :root{
    --stage:#cccccc;
    --paper:#ffffff;
    --brand-blue:#2e3192;
    --brand-orange:#f58a1f;
    --ink-grey:#575757;
    --ink-dark:#333333;
    --frame:#d9d9d9;
  }
  *{margin:0;padding:0;box-sizing:border-box}
  html,body{width:1200px;height:734px;overflow:hidden;background:var(--stage);font-family:'Poppins',sans-serif}
  .flyer{position:absolute;top:54px;width:442px;height:625px;background:var(--paper);overflow:hidden}
  .flyer--filtration{left:126px}
  .flyer--heatpump{left:632px}

  .brand{position:absolute;left:24px;top:22px;display:flex;align-items:center;gap:10px}
  .brand-mark{width:44px;height:44px;background:var(--brand-blue)}
  .brand-name{color:var(--brand-blue);font-weight:700;font-size:17px;line-height:1.05;letter-spacing:-.2px}

  .title-band{position:absolute;left:0;top:75px;width:100%;height:82px;background:var(--brand-blue);color:#fff;padding:10px 0 0 22px}
  .title-band .headline{font-weight:800;font-size:22.5px;line-height:1;letter-spacing:-.2px}
  .title-band .company{font-weight:300;font-size:17px;line-height:1.2;text-transform:uppercase}
  .title-band .tagline{font-weight:700;font-size:18px;line-height:1.05}

  .section-label{position:absolute;left:21px;top:165px;font-size:13px;color:var(--ink-dark);font-weight:400}

  .product-frame{position:absolute;left:22px;width:104px;height:83px;border:1px solid var(--frame);background:#fff;display:flex;align-items:center;justify-content:center}
  .product-shot{border-radius:4px}
  .offer{position:absolute;left:135px;color:var(--ink-grey);font-weight:700;text-transform:uppercase;line-height:1;letter-spacing:-.2px;white-space:nowrap}
  .price{color:var(--brand-orange);font-weight:800;font-size:30px;line-height:1;letter-spacing:-.3px}
  .accent{color:var(--brand-orange)}

  .cta-pill{position:absolute;right:0;background:var(--brand-orange);color:#fff;font-weight:700;text-transform:uppercase;border-radius:18px 0 0 18px;line-height:1;white-space:nowrap}

  .footer{position:absolute;left:0;bottom:0;width:100%;height:63px;background:var(--brand-blue);color:#fff}
  .footer .web{position:absolute;left:22px;top:26px;font-size:10.5px;font-weight:600}
  .footer .call{position:absolute;right:22px;top:9px;display:flex;align-items:center;gap:6px}
  .footer .call-text{line-height:1}
  .footer .call-label{font-weight:300;font-size:15px;display:block}
  .footer .call-number{font-weight:700;font-size:18.5px;display:block;margin-top:2px}

  .hp-photo{position:absolute;left:21px;top:192px;width:135px;height:334px;background:linear-gradient(180deg,#7a3b2e 0%,#8c4a3a 30%,#9a9a9a 55%,#a85a48 100%)}
  .hp-copy{position:absolute;left:172px;width:266px;text-transform:uppercase;line-height:1;letter-spacing:-.2px;white-space:nowrap}
</style>
</head>
<body>

<section class="flyer flyer--filtration">
  <div class="brand"><span class="brand-mark"></span><span class="brand-name">Coral Ridge Pipeworks<br>and Heating</span></div>

  <header class="title-band">
    <div class="headline">WATER FILTRATION SOLUTIONS</div>
    <div class="company">Coral Ridge Pipeworks and Heating</div>
    <div class="tagline">FRESH, CLEAN WATER FOR EVERY TAP</div>
  </header>

  <p class="section-label">Water Filtration Solutions</p>

  <div class="product-frame" style="top:192px"><div class="product-shot" role="img" aria-label="Slim high flow water filter cartridge" style="width:14px;height:66px;background:linear-gradient(180deg,#ddd 0%,#222 20%,#222 100%)"></div></div>
  <div class="offer" style="top:206px">
    <div style="font-size:17px">HIGH FLOW WATER</div>
    <div style="font-size:11px;margin-top:1px">FILTRATION STARTING FROM</div>
    <div class="price" style="margin-left:-4px;margin-top:2px">JUST $550!</div>
  </div>

  <div class="product-frame" style="top:284px"><div class="product-shot" role="img" aria-label="Twin housing whole house water filter" style="width:78px;height:64px;background:linear-gradient(180deg,#3e4347 0%,#3e4347 25%,#7c8288 26%,#6a7076 100%)"></div></div>
  <div class="offer" style="top:285px;font-size:17px">
    <div>WHOLE HOUSE WATER FILTRATION</div>
    <div style="margin-top:1px">ENJOY PURE WATER THROUGHOUT</div>
    <div style="margin-top:1px">YOUR HOME – STARTING FROM</div>
    <div class="price" style="margin-top:0">$1800!</div>
  </div>

  <div class="product-frame" style="top:376px"><div class="product-shot" role="img" aria-label="Whole house filter with UV lamp unit" style="width:38px;height:26px;background:linear-gradient(180deg,#b5b7ba 0%,#b5b7ba 30%,#6a6e72 31%,#6a6e72 100%)"></div></div>
  <div class="offer" style="top:383px">
    <div style="font-size:13.5px">WHOLE HOUSE WATER FILTRATION WITH</div>
    <div style="font-size:12.3px;margin-top:1px">UV LAMP (PERFECT FOR RAINWATER SYSTEMS)</div>
    <div style="font-size:11.3px;margin-top:2px">GET THE ULTIMATE FILTRATION – STARTING FROM</div>
    <div class="price" style="margin-top:1px">$3000!</div>
  </div>

  <div class="product-frame" style="top:469px"><div class="product-shot" role="img" aria-label="Black insulated tumbler cooler" style="width:30px;height:62px;background:linear-gradient(90deg,#111 0%,#333 50%,#111 100%)"></div></div>
  <div class="offer" style="top:480px">
    <div class="accent" style="font-size:14px">FREE BRAVO COOLER</div>
    <div style="font-size:12.5px;margin-top:1px">WITH EVERY WATER</div>
    <div style="font-size:12.5px;margin-top:1px">FILTRATION SYSTEM</div>
    <div style="font-size:18px;margin-top:1px">OR REFERRAL!</div>
  </div>

  <div class="cta-pill" style="top:471px;width:158px;height:82px;padding:8px 0 0 19px">
    <div style="font-size:14.5px">BETTER WATER,</div>
    <div style="font-size:19px">BETTER LIFE</div>
    <div style="font-size:13px;margin-top:1px">CALL NOW FOR A</div>
    <div style="font-size:17.5px;margin-top:2px">FREE QUOTE!</div>
  </div>

  <footer class="footer">
    <span class="web">www.coralridgeph.example.au</span>
    <div class="call">
      <svg width="32" height="34" viewBox="0 0 32 34" aria-hidden="true"><path d="M6 4c2-1 3 0 4 2l2 5c1 2 0 3-1 4l-1 1c1 3 4 7 7 9l1-1c1-1 2-2 4-1l5 3c2 1 2 3 0 5-3 3-7 3-12-1S4 18 3 11C2 8 3 5 6 4z" fill="#fff"/><path d="M17 6a9 9 0 0 1 9 9M17 1a14 14 0 0 1 14 14M17 11a4 4 0 0 1 4 4" stroke="#fff" stroke-width="2" fill="none" stroke-linecap="round"/></svg>
      <span class="call-text"><span class="call-label">CALL US TODAY</span><span class="call-number">0491 837 254</span></span>
    </div>
  </footer>
</section>

<section class="flyer flyer--heatpump">
  <div class="brand"><span class="brand-mark"></span><span class="brand-name">Coral Ridge Pipeworks<br>and Heating</span></div>

  <header class="title-band">
    <div class="headline">HEAT PUMP HOT WATER SYSTEMS</div>
    <div class="company">Coral Ridge Pipeworks and Heating</div>
    <div class="tagline" style="font-size:17.5px">ENERGY-EFFICIENT HOT WATER SOLUTIONS</div>
  </header>

  <p class="section-label">Heat Pump Hot Water Systems</p>

  <div class="hp-photo" role="img" aria-label="Heat pump hot water unit installed against a brick wall"></div>

  <div class="hp-copy accent" style="top:196px;font-weight:700">
    <div style="font-size:13.5px">REBATES AVAILABLE! SAVE BIG WITH</div>
    <div style="font-size:12px;margin-top:1px">GOVERNMENT INCENTIVES ON</div>
    <div style="font-size:12px;margin-top:1px">ENERGY-EFFICIENT HOT WATER SYSTEMS.</div>
  </div>
  <div class="hp-copy" style="top:243px;color:var(--ink-grey);font-weight:700;font-size:16.5px">
    <div>ALL MAJOR MAKES, MODELS,</div>
    <div style="margin-top:1px">AND SIZES WE SUPPLY AND</div>
    <div style="margin-top:1px">INSTALL TRUSTED BRANDS TO</div>
    <div style="margin-top:1px">SUIT YOUR HOUSEHOLD'S NEEDS.</div>
  </div>
  <div class="hp-copy" style="top:327px;font-weight:700">
    <div class="accent" style="font-size:14.5px">INTEREST-FREE FINANCE OPTIONS</div>
    <div style="font-size:15px;color:var(--ink-grey);margin-top:2px">UPGRADE NOW AND PAY LATER</div>
    <div style="font-size:15px;color:var(--ink-grey);margin-top:1px">WITH FLEXIBLE PAYMENT PLANS.</div>
  </div>
  <div class="hp-copy" style="top:386px;font-weight:700">
    <div class="accent" style="font-size:25px;font-weight:800">FREE BRAVO COOLER</div>
    <div style="font-size:20px;color:var(--ink-grey);margin-top:1px">WITH EVERY HEAT PUMP</div>
    <div style="font-size:20px;color:var(--ink-grey);margin-top:2px">SYSTEM OR REFERRAL!</div>
  </div>

  <div class="cta-pill" style="top:472px;width:270px;height:81px;padding:11px 0 0 15px;font-size:20px;line-height:1.05">
    <div>UPGRADE TO ENERGY-</div>
    <div>EFFICIENT HOT WATER</div>
    <div>AND SAVE!</div>
  </div>

  <footer class="footer">
    <span class="web">www.coralridgeph.example.au</span>
    <div class="call">
      <svg width="32" height="34" viewBox="0 0 32 34" aria-hidden="true"><path d="M6 4c2-1 3 0 4 2l2 5c1 2 0 3-1 4l-1 1c1 3 4 7 7 9l1-1c1-1 2-2 4-1l5 3c2 1 2 3 0 5-3 3-7 3-12-1S4 18 3 11C2 8 3 5 6 4z" fill="#fff"/><path d="M17 6a9 9 0 0 1 9 9M17 1a14 14 0 0 1 14 14M17 11a4 4 0 0 1 4 4" stroke="#fff" stroke-width="2" fill="none" stroke-linecap="round"/></svg>
      <span class="call-text"><span class="call-label">CALL US TODAY</span><span class="call-number">0491 837 254</span></span>
    </div>
  </footer>
</section>

</body>
</html>
```